Stationery Design Project - Tarnwell Corporate

Business Cards
Size: 90mm x 55mm
Letterhead
Size: A4 - 210mm x 297mm
With Compliments Slip
Size: DL - 210mm x 99mm
Presentation Folder
Size: A4

Tarnwell Corporate
website: www.tarnwellcorporate.com.au (Under construction)
Offices: *Kelmoor *Ashvale * Dorran

A company that supply Safety consultantcy services

```html
<!DOCTYPE html>
<html lang="en">
<head>
<meta charset="utf-8">
<title>Tarnwell Corporate – Business Cards</title>
<link rel="stylesheet" href="https://fonts.googleapis.com/css2?family=Jost:wght@300;400&family=Arimo:wght@400;700&display=swap">
<style>
  :root {
    --page: #e9e6e2;
    --card-white: #ffffff;
    --ink: #222222;
    --ink-soft: #333333;
    --brand-blue: #1b82c6;
    --band-deep: #0c5fae;
    --band-light: #27c3e4;
    --swoosh: #8a8a8a;
    --charcoal-edge: #2e2e2e;
    --charcoal-glow: #d9d9d9;
    --blue-edge: #0a5ea8;
    --blue-glow: #2ec8ea;
    --white: #ffffff;
  }
  * { box-sizing: border-box; margin: 0; padding: 0; }
  html, body { width: 1200px; height: 787px; overflow: hidden; }
  body { background: var(--page); position: relative; font-family: "Jost", sans-serif; }

  .card {
    position: absolute;
    width: 516px;
    height: 318px;
    overflow: hidden;
    box-shadow: 0 2px 6px rgba(0,0,0,.18);
  }
  .card--front   { left: 62px;  top: 60px;  background: var(--card-white); }
  .card--back    { left: 616px; top: 60px;  background: var(--card-white); }
  .card--charcoal{ left: 66px;  top: 414px; background: radial-gradient(ellipse 300px 200px at 42% 42%, var(--charcoal-glow), #6a6a6a 55%, var(--charcoal-edge)); }
  .card--blue    { left: 611px; top: 414px; background: radial-gradient(ellipse 300px 200px at 50% 42%, var(--blue-glow), #1a8fd0 55%, var(--blue-edge)); }

  .brand {
    position: absolute;
    display: flex;
    align-items: center;
    gap: 12px;
    font-family: "Jost", sans-serif;
    font-weight: 300;
    white-space: nowrap;
  }
  .brand__square { width: 34px; height: 34px; background: var(--brand-blue); flex: none; }

  .card--front .brand { left: 76px; top: 62px; font-size: 36px; color: var(--brand-blue); }
  .address {
    position: absolute; top: 188px; left: 0; width: 100%;
    text-align: center; font-family: "Arimo", sans-serif;
    font-size: 13px; letter-spacing: 1px; color: var(--ink);
  }
  .band { position: absolute; left: 0; top: 210px; width: 516px; height: 108px; }
  .holder {
    position: absolute; top: 256px; left: 0; width: 100%; text-align: center;
    font-family: "Arimo", sans-serif; color: var(--white); font-size: 14px;
  }
  .holder__name { font-weight: 700; font-size: 17px; }
  .contacts {
    position: absolute; top: 294px; left: 0; width: 100%;
    display: flex; justify-content: center; gap: 12px;
    font-family: "Arimo", sans-serif; font-size: 12.5px; color: var(--white);
    white-space: nowrap;
  }
  .contacts span { display: inline-flex; align-items: center; gap: 4px; }
  .contacts svg { width: 10px; height: 10px; }

  .card--back .brand { left: 0; width: 100%; justify-content: center; top: 100px; font-size: 38px; color: var(--brand-blue); }
  .web, .offices {
    position: absolute; left: 0; width: 100%; text-align: center;
    font-family: "Jost", sans-serif; font-weight: 400; white-space: nowrap;
  }
  .offices { display: flex; justify-content: center; align-items: center; }
  .card--back .web { top: 245px; font-size: 20px; color: var(--ink); letter-spacing: .5px; }
  .card--back .offices { top: 287px; font-size: 20px; color: var(--ink-soft); }
  .dot {
    display: inline-block; width: 6px; height: 6px; border-radius: 50%;
    background: currentColor; margin: 0 12px;
  }
  .offices__label { margin-right: 10px; }

  .card--charcoal .brand, .card--blue .brand {
    left: 0; width: 100%; justify-content: center; top: 120px;
    font-size: 50px; color: var(--white); letter-spacing: 1px;
  }
  .card--charcoal .web, .card--blue .web { top: 251px; font-size: 21px; color: var(--white); letter-spacing: .5px; }
  .card--charcoal .offices, .card--blue .offices { top: 292px; font-size: 21px; color: var(--white); }
</style>
</head>
<body>

  <section class="card card--front">
    <div class="brand"><span class="brand__square"></span>Tarnwell Corporate</div>
    <p class="address">00, Complex Name, City, State 0004</p>
    <svg class="band" viewBox="0 0 516 108" aria-hidden="true">
      <defs>
        <linearGradient id="bandFill" x1="0" x2="1" y1="0" y2="0">
          <stop offset="0" stop-color="var(--band-deep)"/>
          <stop offset="1" stop-color="var(--band-light)"/>
        </linearGradient>
      </defs>
      <path d="M0 62 Q258 -26 516 62" fill="none" stroke="var(--swoosh)" stroke-width="5"/>
      <path d="M0 72 Q258 -6 516 72 L516 108 L0 108 Z" fill="url(#bandFill)"/>
    </svg>
    <p class="holder"><span class="holder__name">Daniel Marsh,</span> Business Manager</p>
    <div class="contacts">
      <span><svg viewBox="0 0 10 10"><path d="M2 1 L4 1 L4.5 3 L3.3 4 Q4.5 6 6 6.7 L7 5.5 L9 6 L9 8 Q5 9 1 4 Q1 2 2 1Z" fill="currentColor"/></svg>555-014-2290</span>
      <span><svg viewBox="0 0 10 10"><rect x="1" y="2.5" width="8" height="5.5" fill="none" stroke="currentColor"/><path d="M1 2.5 L5 6 L9 2.5" fill="none" stroke="currentColor"/></svg>info@tarnwellmail.com</span>
      <span><svg viewBox="0 0 10 10"><circle cx="5" cy="5" r="4" fill="none" stroke="currentColor"/><path d="M1 5 H9 M5 1 Q2.5 5 5 9 M5 1 Q7.5 5 5 9" fill="none" stroke="currentColor" stroke-width=".8"/></svg>www.tarnwellcorporate.com.au</span>
    </div>
  </section>

  <section class="card card--back">
    <div class="brand"><span class="brand__square"></span>Tarnwell Corporate</div>
    <p class="web">www.tarnwellcorporate.com.au</p>
    <p class="offices"><span class="offices__label">Offices:</span>Kelmoor<span class="dot"></span>Ashvale<span class="dot"></span>Dorran</p>
  </section>

  <section class="card card--charcoal">
    <div class="brand">Tarnwell Corporate</div>
    <p class="web">www.tarnwellcorporate.com.au</p>
    <p class="offices"><span class="offices__label">Offices:</span>Kelmoor<span class="dot"></span>Ashvale<span class="dot"></span>Dorran</p>
  </section>

  <section class="card card--blue">
    <div class="brand">Tarnwell Corporate</div>
    <p class="web">www.tarnwellcorporate.com.au</p>
    <p class="offices"><span class="offices__label">Offices:</span>Kelmoor<span class="dot"></span>Ashvale<span class="dot"></span>Dorran</p>
  </section>

</body>
</html>
```